Tomo Rasu bar restaurant japanese street food

Hello dear friends!

We are a Gyoza Bar, specializing in square sandwiches (made with Hokkaido bread) and gyoza dumplings.

Our interior is designed to look like a Japanese street, with many signboards, street signs, and urban elements. We will attach photos so you can capture the overall vibe and atmosphere.

Our kitchen concept is street food.

Today we have a task to develop a takeaway / delivery box for our food.

We truly love our product and want to give it a professional and distinctive presentation.

Custom packaging is an important part of our brand style.

We appreciate non-standard solutions, shapes, and sizes.

About our product
We are a Gyoza Bar, and we have several types of gyoza:

Beef

Pork

Chicken

Vegetable

Salmon & Shrimp

What we need
We need one universal box for all flavors, with flavor indicators that we can mark when assembling an order.

A standard portion contains 6 dumplings.

Size of one dumpling:

Length: 7.5 cm

Height: 3.5 cm

Inside the box
The box must include:

An integrated sauce container

Diameter: 6 cm

Height: 3 cm

Shape: wider toward the top than the bottom

Chopsticks placed inside the box

Dividers between dumplings so they do not stick together

We imagine the box as a long rectangular shape.

Multiple portions
If an order includes several portions, the boxes should be able to connect or stack together.

For example:

stacking one box on top of another

small locking tabs or “ears” that allow the boxes to be connected together

You will see reference examples in the attachments.

Design
The design direction is up to you, as we like both:

minimalist concepts

more detailed / graphic designs

The most important thing is:
please do not make the logo too small, because it needs to remain clearly readable.

Final deliverable
The final result should be a packaging dieline (flat layout) that we can send directly to production without additional questions.

Thank you all for your attention and good luck!
If you have any questions, we will be happy to answer them.

P.S.

We also need a second box for other dishes with the following dimensions:

12.5 cm × 12.5 cm
Height: 7 cm

Target Market(s)

Please note that we are a high-quality street food brand. Packaging is part of our identity. We communicate through packaging

Requirements
Must have
• Chopsticks and a sauce container must be integrated into the packaging.

```html
<!DOCTYPE html>
<html lang="en">
<head>
<meta charset="utf-8">
<title>Tomo Rasu – Gyoza Box Lid</title>
<link rel="stylesheet" href="https://fonts.googleapis.com/css2?family=Montserrat:wght@700&display=swap">
<style>
  :root {
    --stage: #2a2624;
    --neon-pink: #d8338f;
    --neon-magenta: #b02a9a;
    --neon-red: #d3232e;
    --neon-blue: #2d3f8f;
    --neon-green: #1f9a5a;
    --neon-yellow: #f1c420;
    --sign-white: #ecebe6;
    --night: #1a1620;
    --window: #f2f1ef;
    --divider: #6d6d6d;
    --badge: #141414;
    --badge-edge: #e9e9e9;
    --badge-text: #ffffff;
    --fold: rgba(0, 0, 0, 0.35);
  }
  html, body {
    margin: 0;
    width: 1200px;
    height: 1200px;
    overflow: hidden;
    background: var(--stage);
  }
  .canvas {
    position: relative;
    width: 1200px;
    height: 1200px;
  }
  .box-net {
    position: absolute;
    left: 45px;
    top: 365px;
    width: 1110px;
    height: 470px;
  }
  .panel {
    position: absolute;
    overflow: hidden;
  }
  .panel-lid   { left: 0; top: 0; width: 1000px; height: 360px; }
  .panel-front { left: 0; top: 360px; width: 1000px; height: 110px; border-top: 2px dashed var(--fold); box-sizing: border-box; }
  .panel-end   { left: 1000px; top: 0; width: 110px; height: 360px; border-left: 2px dashed var(--fold); box-sizing: border-box; }

  .signboard-collage {
    position: absolute;
    inset: 0;
    background:
      linear-gradient(90deg,
        var(--neon-blue) 0 6%, var(--sign-white) 6% 12%, var(--neon-pink) 12% 19%,
        var(--night) 19% 22%, var(--neon-yellow) 22% 27%, var(--neon-magenta) 27% 35%,
        var(--sign-white) 35% 41%, var(--night) 41% 44%, var(--neon-red) 44% 52%,
        var(--neon-blue) 52% 58%, var(--sign-white) 58% 64%, var(--neon-green) 64% 71%,
        var(--neon-red) 71% 79%, var(--sign-white) 79% 85%, var(--neon-blue) 85% 91%,
        var(--neon-red) 91% 100%) 0 0 / 100% 34% no-repeat,
      linear-gradient(90deg,
        var(--neon-green) 0 5%, var(--sign-white) 5% 11%, var(--neon-red) 11% 16%,
        var(--neon-blue) 16% 23%, var(--sign-white) 23% 30%, var(--neon-pink) 30% 38%,
        var(--night) 38% 42%, var(--neon-yellow) 42% 47%, var(--sign-white) 47% 55%,
        var(--neon-red) 55% 62%, var(--neon-green) 62% 69%, var(--neon-blue) 69% 74%,
        var(--sign-white) 74% 81%, var(--neon-red) 81% 88%, var(--neon-green) 88% 94%,
        var(--neon-red) 94% 100%) 0 34% / 100% 33% no-repeat,
      linear-gradient(90deg,
        var(--neon-red) 0 4%, var(--neon-green) 4% 9%, var(--neon-magenta) 9% 18%,
        var(--sign-white) 18% 25%, var(--neon-blue) 25% 31%, var(--neon-yellow) 31% 36%,
        var(--night) 36% 40%, var(--sign-white) 40% 47%, var(--neon-pink) 47% 55%,
        var(--neon-blue) 55% 61%, var(--neon-red) 61% 68%, var(--sign-white) 68% 75%,
        var(--neon-green) 75% 82%, var(--neon-red) 82% 90%, var(--neon-blue) 90% 95%,
        var(--sign-white) 95% 100%) 0 100% / 100% 34% no-repeat,
      var(--night);
  }
  .panel-front .signboard-collage,
  .panel-end .signboard-collage { filter: brightness(0.78); }

  .dumpling-window {
    position: absolute;
    left: 70px;
    top: 95px;
    width: 640px;
    height: 140px;
    background: var(--window);
    display: grid;
    grid-template-columns: repeat(6, 1fr);
  }
  .dumpling-cell + .dumpling-cell {
    border-left: 2px dashed var(--divider);
  }
  .sauce-window {
    position: absolute;
    left: 780px;
    top: 18px;
    width: 200px;
    height: 200px;
    border-radius: 50%;
    background: var(--window);
  }
  .brand-badge {
    position: absolute;
    left: 400px;
    top: 258px;
    padding: 14px 30px;
    background: var(--badge);
    border: 4px solid var(--badge-edge);
    border-radius: 14px;
    color: var(--badge-text);
    font-family: "Montserrat", sans-serif;
    font-weight: 700;
    font-size: 38px;
    letter-spacing: 2px;
    line-height: 1;
    white-space: nowrap;
  }
</style>
</head>
<body>
  <main class="canvas">
    <section class="box-net">
      <div class="panel panel-lid">
        <div class="signboard-collage" role="img" aria-label="Dense collage of glowing Japanese street signboards in pink, red, blue, green, yellow and white"></div>
        <div class="dumpling-window">
          <div class="dumpling-cell"></div>
          <div class="dumpling-cell"></div>
          <div class="dumpling-cell"></div>
          <div class="dumpling-cell"></div>
          <div class="dumpling-cell"></div>
          <div class="dumpling-cell"></div>
        </div>
        <div class="sauce-window"></div>
        <div class="brand-badge">TOMO RASU</div>
      </div>
      <div class="panel panel-front">
        <div class="signboard-collage" role="img" aria-label="Side panel continuing the neon street signboard collage"></div>
      </div>
      <div class="panel panel-end">
        <div class="signboard-collage" role="img" aria-label="End panel continuing the neon street signboard collage"></div>
      </div>
    </section>
  </main>
</body>
</html>
```